bramlo-vista virtual tours is looking for a website redisgn that uses our new logo

Using BVT's logo as a basis, please redesign our website. Our web application developer has a stand-in site up at www.bl-vista.example. BVT is a virtual tour company whose main clients are the owners of real estate and rental properties; however, BVT will produce virtual tours for any person, company, or organization for whatever purpose they see fit to use the tour for. This is a dynamic website consisting of three pages. An index/info page, a contact/web form page, a price listing page, a template for a tour page which will have a height/width 75% iframe that showcases one of our tours (www.bl-vista.example) for an example. What is needed: HTML template design for pages that incorporates logo, custom graphic for mail link, PB link, Chirpster link, and Virtual Tour link. We would also like a watermarked developed out of our logo pin (.ai of logo pin included). The watermark should also include the capital letters BVT, be in grayscale, translucent and the masked.
Target Market(s)
Home Owners, Real Estate Agents, Property Managers, Event Managers, Business Owners, Park Owners,
Industry/Entity Type
Real Estate
Number of Pages Required
3 page
Font styles to use
Requirements
Must have
- New web design that uses our logo (file included). Must have a custom watermark that uses our custom logo pin (file included). Watermark should be gray scale, translucent, and masked. Custom graphics for homepage link (would like something that uses our logo pin), mail link, pinbook link, and chirpster link.
Nice to have
- I've uploaded a pdf called pano_vs_spherical.pdf which is a scan of a crude drawing I did that illustrates what we'd like for our info page. Basically we'd like to describe the difference between a panoramic image and a spherical image and to do so we'd like to have some graphical drawings that illustrate which each is. We'd like two separate image files that we can include on our info page. Use the uploaded .pdf as a guide. Would also like images 0-9 of custom numerals that match the theme of the page to be used as part of a visitor counter script.
Should not have
- Do not need html code or stylesheets (css). Would rather you concentrate on graphic design of custom graphics, layout, and color scheme. We have competent web applications developers in our small company who can code, we just need you, the graphic artist to work your magic.

```html
<!DOCTYPE html>
<html lang="en">
<head>
<meta charset="utf-8">
<title>Bramlo-vista Virtual Tours</title>
<link rel="stylesheet" href="https://fonts.googleapis.com/css2?family=Oswald:wght@600&family=Play:wght@400;700&family=Open+Sans:wght@400;600;700&display=swap">
<style>
  :root {
    --page-grey: #7b808c;
    --page-grey-light: #a9adb6;
    --page-grey-dark: #5f646f;
    --nav-black: #121212;
    --accent-orange: #ee6a1f;
    --ink-dark: #1d1d1f;
    --white: #ffffff;
    --bar-grey: #5a5d63;
    --bar-dark: #3b3d42;
    --field-grey: #c9cbcf;
    --footer-dark: #3f434c;
  }
  * { box-sizing: border-box; margin: 0; padding: 0; }
  html, body { width: 1200px; height: 900px; overflow: hidden; }
  body {
    position: relative;
    font-family: "Open Sans", sans-serif;
    color: var(--white);
    background:
      radial-gradient(ellipse 520px 130px at 600px 50px, rgba(255,255,255,0.45), rgba(255,255,255,0) 100%),
      linear-gradient(180deg, var(--page-grey-light) 0%, var(--page-grey) 14%, var(--page-grey) 70%, var(--page-grey-dark) 100%);
  }

  /* Header / brand */
  .site-header { position: absolute; left: 0; top: 0; width: 1200px; height: 121px; }
  .brand {
    position: absolute; left: 470px; top: 24px;
    display: flex; align-items: center; gap: 12px;
  }
  .brand-dot { width: 46px; height: 46px; border-radius: 50%; background: var(--accent-orange); }
  .brand-text { display: flex; flex-direction: column; align-items: flex-end; }
  .brand-name {
    font-family: "Play", sans-serif; font-weight: 700; font-size: 36px;
    line-height: 1; color: var(--ink-dark); letter-spacing: -0.5px;
  }
  .brand-tagline {
    font-family: "Open Sans", sans-serif; font-weight: 700; font-size: 9px;
    color: var(--accent-orange); letter-spacing: 0.5px; margin-top: 2px;
  }

  /* Navigation */
  .main-nav {
    position: absolute; left: 0; top: 121px; width: 1200px; height: 40px;
    background: var(--nav-black);
  }
  .nav-links { position: absolute; left: 200px; top: 0; display: flex; list-style: none; height: 40px; }
  .nav-links li {
    height: 40px; display: flex; align-items: center; justify-content: center;
    font-size: 14px; border-right: 1px solid #2c2c2c; color: var(--white);
  }
  .nav-links .nav-home { width: 92px; background: var(--accent-orange); color: var(--ink-dark); }
  .nav-links .nav-contact { width: 130px; }
  .nav-links .nav-pricing { width: 104px; }
  .social-links { position: absolute; left: 894px; top: 5px; display: flex; gap: 7px; }
  .social-links svg { display: block; }

  /* Tour viewer */
  .tour-view {
    position: absolute; left: 0; top: 161px; width: 1200px; height: 374px;
    background:
      linear-gradient(180deg, rgba(255,255,255,0.05) 0%, rgba(0,0,0,0.15) 55%, rgba(230,230,230,0.55) 100%),
      linear-gradient(90deg, #6b6b6b 0%, #8a7a6c 30%, #b79c86 42%, #a6a6a6 58%, #cfcfcf 80%, #777 100%);
  }
  .tour-controls {
    position: absolute; left: 0; top: 535px; width: 1200px; height: 50px;
    background: linear-gradient(180deg, #6a6d73 0%, var(--bar-grey) 100%);
  }
  .tour-controls-dark {
    position: absolute; left: 555px; top: 0; width: 645px; height: 50px;
    background: linear-gradient(180deg, #4a4d52 0%, var(--bar-dark) 100%);
    clip-path: polygon(26px 0, 100% 0, 100% 100%, 0 100%);
  }
  .tour-mark {
    position: absolute; left: 213px; top: 13px; display: flex; align-items: center; gap: 6px;
  }
  .tour-mark-dot { width: 22px; height: 22px; border-radius: 50%; background: #8d9096; }
  .tour-mark-name { font-family: "Play", sans-serif; font-weight: 700; font-size: 20px; color: #8d9096; }
  .tour-buttons { position: absolute; left: 597px; top: 10px; display: flex; gap: 4.5px; }
  .tour-buttons svg { display: block; }

  /* Info row */
  .info-row { position: absolute; left: 0; top: 623px; width: 1200px; height: 36px; }
  .view-counter {
    position: absolute; left: 215px; top: 0; width: 334px; height: 36px;
    background: linear-gradient(180deg, #e3e4e6, var(--field-grey));
    border: 2px solid #9a9da3; border-radius: 3px;
    display: flex; align-items: center; padding-left: 16px; color: var(--ink-dark);
  }
  .counter-digits { font-family: "Oswald", sans-serif; font-weight: 600; font-size: 25px; letter-spacing: 0.5px; }
  .counter-label { font-size: 17px; margin-left: 6px; }
  .full-screen-button {
    position: absolute; left: 576px; top: 0; width: 184px; height: 36px;
    background: linear-gradient(180deg, #ffffff, #dadbdd); border-radius: 3px;
    display: flex; align-items: center; justify-content: center; gap: 8px;
    font-size: 17px; color: var(--ink-dark);
  }
  .scene-select {
    position: absolute; left: 812px; top: 0; width: 174px; height: 36px;
    background: linear-gradient(180deg, #b5b8bd, #9ea2a8); border-radius: 3px;
    display: flex; align-items: center; padding-left: 12px;
    font-size: 15px; color: var(--ink-dark);
  }
  .scene-select svg { position: absolute; right: 12px; top: 14px; }

  /* Welcome */
  .welcome { position: absolute; left: 248px; top: 680px; width: 704px; text-align: center; }
  .welcome-title {
    font-family: "Play", sans-serif; font-weight: 700; font-size: 26px;
    color: var(--white); text-shadow: 0 1px 2px rgba(0,0,0,0.35); padding-bottom: 10px;
    border-bottom: 1px solid rgba(255,255,255,0.35); width: 610px; margin: 0 auto;
  }
  .welcome-text { font-size: 12.3px; line-height: 20px; margin-top: 12px; color: #f4f4f4; }
  .welcome-text strong { font-weight: 700; }

  /* Footer */
  .site-footer {
    position: absolute; left: 0; top: 848px; width: 1200px; height: 52px;
    background: linear-gradient(180deg, #4a4e58, var(--footer-dark));
    display: flex; align-items: center; justify-content: center;
    font-size: 11px; color: #e6e6e6;
  }
  .site-footer span { margin: 0 7px; }
</style>
</head>
<body>

<header class="site-header">
  <div class="brand">
    <div class="brand-dot"></div>
    <div class="brand-text">
      <span class="brand-name">bramlo-vista</span>
      <span class="brand-tagline">VIRTUAL TOURS</span>
    </div>
  </div>
</header>

<nav class="main-nav">
  <ul class="nav-links">
    <li class="nav-home">HOME</li>
    <li class="nav-contact">CONTACT US</li>
    <li class="nav-pricing">PRICING</li>
  </ul>
  <div class="social-links">
    <svg width="28" height="30" viewBox="0 0 28 30" role="img" aria-label="pinbook link">
      <circle cx="14" cy="14" r="13" fill="#d7d9dc" stroke="#fff" stroke-width="1.5"/>
      <text x="14" y="18" text-anchor="middle" font-family="Open Sans, sans-serif" font-size="10" font-weight="700" fill="#4a4d52">PB</text>
    </svg>
    <svg width="28" height="30" viewBox="0 0 28 30" role="img" aria-label="chirpster link">
      <circle cx="14" cy="14" r="13" fill="#d7d9dc" stroke="#fff" stroke-width="1.5"/>
      <text x="14" y="18" text-anchor="middle" font-family="Open Sans, sans-serif" font-size="10" font-weight="700" fill="#4a4d52">CH</text>
    </svg>
    <svg width="28" height="30" viewBox="0 0 28 30" role="img" aria-label="mail link">
      <circle cx="14" cy="14" r="13" fill="#d7d9dc" stroke="#fff" stroke-width="1.5"/>
      <rect x="7.5" y="9.5" width="13" height="9" fill="#4a4d52"/>
      <path d="M7.5 9.5 L14 15 L20.5 9.5" fill="none" stroke="#d7d9dc" stroke-width="1.2"/>
    </svg>
  </div>
</nav>

<section class="tour-view" role="img" aria-label="Spherical panorama of a church interior with pews and arches, with a camera in front showing the same view"></section>

<div class="tour-controls">
  <div class="tour-controls-dark"></div>
  <div class="tour-mark">
    <div class="tour-mark-dot"></div>
    <span class="tour-mark-name">bvt</span>
  </div>
  <div class="tour-buttons">
    <svg width="30" height="30" viewBox="0 0 30 30" aria-label="zoom in"><circle cx="15" cy="15" r="13" fill="none" stroke="#fff" stroke-width="2"/><path d="M15 8v14M8 15h14" stroke="#fff" stroke-width="3"/></svg>
    <svg width="30" height="30" viewBox="0 0 30 30" aria-label="zoom out"><circle cx="15" cy="15" r="13" fill="none" stroke="#fff" stroke-width="2"/><path d="M8 15h14" stroke="#fff" stroke-width="3"/></svg>
    <svg width="30" height="30" viewBox="0 0 30 30" aria-label="look down"><circle cx="15" cy="15" r="13" fill="none" stroke="#fff" stroke-width="2"/><path d="M12 7h6v8h4l-7 8-7-8h4z" fill="#fff"/></svg>
    <svg width="30" height="30" viewBox="0 0 30 30" aria-label="look up"><circle cx="15" cy="15" r="13" fill="none" stroke="#fff" stroke-width="2"/><path d="M12 23h6v-8h4l-7-8-7 8h4z" fill="#fff"/></svg>
    <svg width="30" height="30" viewBox="0 0 30 30" aria-label="look left"><circle cx="15" cy="15" r="13" fill="none" stroke="#fff" stroke-width="2"/><path d="M23 12v6h-8v4l-8-7 8-7v4z" fill="#fff"/></svg>
    <svg width="30" height="30" viewBox="0 0 30 30" aria-label="look right"><circle cx="15" cy="15" r="13" fill="none" stroke="#fff" stroke-width="2"/><path d="M7 12v6h8v4l8-7-8-7v4z" fill="#fff"/></svg>
    <svg width="30" height="30" viewBox="0 0 30 30" aria-label="drag mode"><circle cx="15" cy="15" r="13" fill="#2f3135" stroke="#6b6e73" stroke-width="2"/><rect x="10" y="9" width="10" height="12" rx="4" fill="#6b6e73"/></svg>
    <svg width="30" height="30" viewBox="0 0 30 30" aria-label="auto rotate"><circle cx="15" cy="15" r="13" fill="none" stroke="#fff" stroke-width="2"/><path d="M21 12a7 7 0 1 0 0.5 5" fill="none" stroke="#fff" stroke-width="2.5"/><path d="M22 7v6h-6z" fill="#fff"/></svg>
    <svg width="30" height="30" viewBox="0 0 30 30" aria-label="help"><circle cx="15" cy="15" r="13" fill="none" stroke="#fff" stroke-width="2"/><text x="15" y="21" text-anchor="middle" font-family="Open Sans, sans-serif" font-size="17" font-weight="700" fill="#fff">?</text></svg>
    <svg width="30" height="30" viewBox="0 0 30 30" aria-label="hide hotspots"><circle cx="15" cy="15" r="13" fill="none" stroke="#fff" stroke-width="2"/><path d="M7 15q8-8 16 0q-8 8-16 0z" fill="none" stroke="#fff" stroke-width="2"/><circle cx="15" cy="15" r="2.5" fill="#fff"/><path d="M9 22L21 8" stroke="#fff" stroke-width="2"/></svg>
    <svg width="30" height="30" viewBox="0 0 30 30" aria-label="sound"><circle cx="15" cy="15" r="13" fill="none" stroke="#fff" stroke-width="2"/><path d="M8 12h4l5-4v14l-5-4h-4z" fill="#fff"/><path d="M19.5 11.5q2.5 3.5 0 7" fill="none" stroke="#fff" stroke-width="1.8"/></svg>
  </div>
</div>

<div class="info-row">
  <div class="view-counter">
    <span class="counter-digits">72,823,647</span>
    <span class="counter-label">- VIRTUAL SHOWINGS</span>
  </div>
  <div class="full-screen-button">
    <svg width="14" height="14" viewBox="0 0 14 14" aria-hidden="true"><path d="M1 1h4L1 5zM13 1v4L9 1zM1 13V9l4 4zM13 13H9l4-4z" fill="#1d1d1f"/><path d="M2 2l10 10M12 2L2 12" stroke="#1d1d1f" stroke-width="1.5"/></svg>
    VIEW FULL SCREEN
  </div>
  <div class="scene-select">
    FRONT ENTRY
    <svg width="16" height="9" viewBox="0 0 16 9" aria-hidden="true"><path d="M0 0h16L8 9z" fill="#6e7278"/></svg>
  </div>
</div>

<section class="welcome">
  <h1 class="welcome-title">Welcome to Bramlo-vista Virtual Tours</h1>
  <p class="welcome-text">Sed ut perspiciatis unde omnis iste natus error sit voluptatem accusantium doloremque laudantium, totam rem aperiam, eaque ipsa quae ab illo inventore veritatis et quasi <strong>architecto</strong> beatae vitae dicta sunt explicabo. Nemo enim ipsam voluptatem quia voluptas sit aspernatur aut odit aut fugit, sed quia conseq dfhdsrtyhjntur magni dolores eos qui ratione voluptatem sequi nesciunt. Neque porro quisquam est, qui dolorem ipsum quia dolor sit amet, consectetur, adipisci velit, sed quia non numquam eius.</p>
</section>

<footer class="site-footer">
  <span>© 2015. Bramlo-vista Virtual Tours</span>|<span>Terms &amp; Conditions</span>|<span>Privacy Policy.</span>
</footer>

</body>
</html>
```